I need a business card design for a Boutique Pilates studio.

I would like to see designs similar to the one that I have uploaded.
thinking between two slogans:
'No ordinary place'
'Not so ordinary'

Contact Information for Business Card

KiVa Pilates

```html
<!DOCTYPE html>
<html lang="en">
<head>
<meta charset="UTF-8">
<title>KiVa Pilates – Business Card</title>
<link href="https://fonts.googleapis.com/css2?family=Poppins:wght@300;400;600&display=swap" rel="stylesheet">
<style>
  :root {
    --backdrop: #232323;
    --card: #0b0b0b;
    --card-edge: #e2cf12;
    --gold: #d8c20f;
    --silver: #e8e8e8;
    --rule: #4a4a4a;
  }
  * { margin: 0; padding: 0; box-sizing: border-box; }
  html, body { width: 1200px; height: 900px; overflow: hidden; }
  body {
    background: var(--backdrop);
    display: flex;
    flex-direction: column;
    align-items: center;
    justify-content: center;
    gap: 36px;
    font-family: "Poppins", sans-serif;
  }
  .card {
    position: relative;
    width: 700px;
    height: 400px;
    background: var(--card);
    border-radius: 26px;
    border-bottom: 5px solid var(--card-edge);
    overflow: hidden;
  }
  .brand {
    position: absolute;
    display: flex;
    justify-content: center;
    align-items: center;
  }
  .brand-name {
    font-family: "Poppins", sans-serif;
    font-weight: 300;
    letter-spacing: 2px;
    line-height: 1;
    white-space: nowrap;
  }
  /* Logo side */
  .card-logo .brand { left: 0; right: 0; top: 0; height: 360px; }
  .card-logo .brand-name { font-size: 58px; color: var(--silver); }

  /* Contact side */
  .card-contact .brand { left: 20px; width: 290px; top: 0; height: 400px; }
  .card-contact .brand-name { font-size: 40px; color: var(--gold); }
  .divider {
    position: absolute;
    left: 330px;
    top: 70px;
    width: 1px;
    height: 260px;
    background: var(--rule);
  }
  .contact {
    position: absolute;
    left: 365px;
    top: 88px;
    color: var(--gold);
  }
  .contact-name { font-size: 27px; font-weight: 600; line-height: 1.1; }
  .contact-role { font-size: 17px; font-weight: 300; margin-bottom: 22px; }
  .contact-list { list-style: none; }
  .contact-list li {
    display: flex;
    align-items: center;
    gap: 10px;
    font-size: 16px;
    font-weight: 300;
    line-height: 1.6;
  }
  .contact-list svg { width: 16px; height: 16px; flex: none; }
  .contact-address {
    font-size: 16px;
    font-weight: 300;
    line-height: 1.4;
    margin-top: 16px;
    padding-left: 26px;
    font-style: normal;
  }
</style>
</head>
<body>
  <section class="card card-logo">
    <div class="brand">
      <span class="brand-name">KiVa Pilates</span>
    </div>
  </section>

  <section class="card card-contact">
    <div class="brand">
      <span class="brand-name">KiVa Pilates</span>
    </div>
    <div class="divider"></div>
    <div class="contact">
      <p class="contact-name">Marcus Hale</p>
      <p class="contact-role">Managing Director</p>
      <ul class="contact-list">
        <li>
          <svg viewBox="0 0 16 16" aria-hidden="true"><path d="M3.5 1.5 L6 4 L4.8 6 Q6.5 9.5 10 11.2 L12 10 L14.5 12.5 L12.8 14.4 Q6.5 13.8 1.6 3.2 Z" fill="var(--gold)"/></svg>
          021-555 018 642
        </li>
        <li>
          <svg viewBox="0 0 16 16" aria-hidden="true"><rect x="1" y="3" width="14" height="10" fill="var(--gold)"/><path d="M1 3 L8 9 L15 3" stroke="var(--card)" stroke-width="1.2" fill="none"/></svg>
          hello@kivastudio.com
        </li>
        <li>
          <svg viewBox="0 0 16 16" aria-hidden="true"><circle cx="8" cy="8" r="7" fill="var(--gold)"/><g stroke="var(--card)" stroke-width="0.9" fill="none"><ellipse cx="8" cy="8" rx="3" ry="7"/><line x1="1" y1="8" x2="15" y2="8"/><line x1="2.2" y1="4.5" x2="13.8" y2="4.5"/><line x1="2.2" y1="11.5" x2="13.8" y2="11.5"/></g></svg>
          www.kivastudio.com
        </li>
      </ul>
      <address class="contact-address">421, Address line goes here<br>45452,Country Name</address>
    </div>
  </section>
</body>
</html>
```